依頼詳細
ノンシリコンスカルプシャンプー
頭皮をしっかり洗浄し傷ついた髪の毛を修復します。
またアロマ系の香りがリラックス効果を促します。
ユニセックスシャンプーですが女性向けでば珍しいブラックボトルを採用し、
Tovrena(輝く私)の名称通りしなやかで芯のある女性をイメージしたパッケージラベル
記載項目
サイズ:W35㎜×P65㎜
防水シール
希望イメージ
シンプル 複雑
単色 カラフル
暗い 明るい
日常 高級
遊び心 厳粛
未来的 伝統的
女性的 男性的
希望する色
設定なし
納品ファイル
• 高解像度JPG (.jpg)
• イラストレーター形式 (.ai)
• フォトショップ形式 (.psd)
• PNG形式 (.png)
補足説明
設定なし
製品名『Tovrena Premium Shampoo』の文字デザインをメインにお願いします。
参考までに他社のボトルラベルの画像をUPします。
文字だけのデザインを希望しています。
■ 選んだ理由

シャンプーを使った時に感じてもらうイメージがシンプルでスッキリとしたデザインとマッチしている点です。対象のお客様もほどんどが女性の為、女性らしい書体デザインが気に入りました。

■ 提案者全員のお礼・コメント

たくさんの方に提案を頂き本当に感謝しています。ありがとうございました。
選定には大変迷いましたが素敵なデザインをたくさん目にすることができて本当に良かったです。皆様の今後の活躍を心より祈願します。

```html
<!DOCTYPE html>
<html lang="en">
<head>
<meta charset="utf-8">
<title>Tovrena Premium Shampoo — Label</title>
<link rel="stylesheet" href="https://fonts.googleapis.com/css2?family=Cormorant+Garamond:wght@500;600&family=Cormorant+SC:wght@500&family=Parisienne&display=swap">
<style>
  :root {
    --backdrop: #e9e9e9;
    --label: #ffffff;
    --ink: #2a2a2a;
    --ink-soft: #3c3c3c;
  }
  * { margin: 0; padding: 0; box-sizing: border-box; }
  html, body {
    width: 1200px;
    height: 2492px;
    overflow: hidden;
    background: var(--backdrop);
  }
  .label {
    position: absolute;
    left: 100px;
    top: 317px;
    width: 1000px;
    height: 1857px;
    background: var(--label);
    color: var(--ink);
    text-align: center;
  }
  .brand-name {
    position: absolute;
    top: 150px;
    width: 100%;
    font-family: "Cormorant SC", serif;
    font-weight: 500;
    font-size: 118px;
    letter-spacing: 8px;
  }
  .product-name {
    position: absolute;
    top: 330px;
    width: 100%;
    font-family: "Cormorant Garamond", serif;
    font-weight: 600;
    font-size: 74px;
    letter-spacing: 3px;
  }
  .divider {
    position: absolute;
    top: 500px;
    left: 250px;
    width: 500px;
    height: 30px;
  }
  .description {
    position: absolute;
    top: 620px;
    left: 120px;
    width: 760px;
    font-family: "Parisienne", cursive;
    font-size: 50px;
    line-height: 1.45;
    color: var(--ink-soft);
  }
  .specs {
    position: absolute;
    bottom: 70px;
    width: 100%;
    font-family: "Cormorant Garamond", serif;
    font-weight: 500;
    font-size: 48px;
    line-height: 1.3;
  }
</style>
</head>
<body>
  <main class="label">
    <h1 class="brand-name">Tovrena</h1>
    <p class="product-name">Premium Shampoo</p>
    <svg class="divider" viewBox="0 0 500 30" aria-hidden="true">
      <line x1="20" y1="15" x2="480" y2="15" stroke="#2a2a2a" stroke-width="3"/>
      <rect x="10" y="7" width="16" height="16" transform="rotate(45 18 15)" fill="#2a2a2a"/>
      <rect x="474" y="7" width="16" height="16" transform="rotate(45 482 15)" fill="#2a2a2a"/>
    </svg>
    <p class="description">Clean the scalp firmly and repair damaged hair. The fragrance of the aroma series also invites a relaxing effect.</p>
    <p class="specs">Non Silicon<br>Bergamot<br>400mL</p>
  </main>
</body>
</html>
```